New Book Cover for Website Advertising

I need a new book cover design to go on my website to generate pre-orders before my book is published. I have a previous design which I think needs a refresh. I want the new cover to complement the colours of my new website and logo. I'll attach the old book cover. All the words will remain the same, I just need an entirely new design

Target Market(s)

Corporate Leaders

Industry/Entity Type

Human resources

Font styles to use
Sans Serif

Colors
F0912C
F2A743
F7CA91
FBE8D2
FDF5EE
6B429C
8869AF
B7A5CE
E3DAEB
F3F0F8

Requirements
Must have
• A feeling of lightness, not dark
Should not have
• Any clip art or common stock photos

```html
<!DOCTYPE html>
<html lang="en">
<head>
<meta charset="utf-8">
<title>The Secure Leader — Tova Lund</title>
<link rel="stylesheet" href="https://fonts.googleapis.com/css2?family=Anton&family=Oswald:wght@500&family=Poppins:wght@500&display=swap">
<style>
  :root {
    --mint: #cfe3d7;
    --cream: #e9ebd8;
    --wood-light: #eedcb8;
    --wood-dark: #d9c29a;
    --lavender: #9f8bc3;
    --ink: #111111;
    --coral: #e07b55;
    --white: #ffffff;
    --plum: #4b2a86;
  }
  * { margin: 0; padding: 0; box-sizing: border-box; }
  html, body { width: 800px; height: 1200px; overflow: hidden; }
  body { background: var(--cream); }
  .cover {
    position: relative;
    width: 800px;
    height: 1200px;
    overflow: hidden;
    background: linear-gradient(180deg, var(--mint) 0%, #d3e5d6 45%, #e6ebd8 65%, var(--cream) 100%);
  }
  .cover__photo {
    position: absolute;
    left: 0; top: 0;
    width: 800px; height: 760px;
  }
  .cover__title {
    position: absolute;
    left: 50px; top: 36px;
    font-family: "Anton", "Oswald", sans-serif;
    font-weight: 400;
    font-size: 125px;
    line-height: 130px;
    color: var(--lavender);
    text-shadow: 3px 3px 0 var(--ink);
    letter-spacing: -1px;
    white-space: nowrap;
  }
  .cover__title span { display: block; }
  .cover__subtitle {
    position: absolute;
    right: 85px; top: 760px;
    text-align: right;
    font-family: "Oswald", sans-serif;
    font-weight: 500;
    font-size: 34px;
    line-height: 46px;
    color: var(--coral);
    white-space: nowrap;
  }
  .cover__subtitle span { display: block; }
  .cover__author {
    position: absolute;
    right: 82px; top: 1028px;
    font-family: "Anton", "Oswald", sans-serif;
    font-weight: 400;
    font-size: 125px;
    line-height: 130px;
    color: var(--lavender);
    text-shadow: 3px 3px 0 var(--ink);
    letter-spacing: -1px;
    white-space: nowrap;
  }
  .publisher {
    position: absolute;
    left: 51px; top: 1047px;
    width: 106px; height: 106px;
    background: var(--white);
    display: flex;
    align-items: center;
    justify-content: center;
  }
  .publisher__name {
    font-family: "Poppins", sans-serif;
    font-weight: 500;
    font-size: 12px;
    color: var(--plum);
  }
</style>
</head>
<body>
  <main class="cover">
    <svg class="cover__photo" viewBox="0 0 800 760" role="img" aria-label="Photo of wooden blocks stacked as steps with tick marks, a hand placing a flag block on top">
      <defs>
        <linearGradient id="wood" x1="0" y1="0" x2="0" y2="1">
          <stop offset="0" stop-color="#eedcb8"/>
          <stop offset="1" stop-color="#d9c29a"/>
        </linearGradient>
      </defs>
      <polygon fill="url(#wood)" points="94,747 94,594 247,594 247,444 395,444 395,293 708,293 711,444 714,594 714,747"/>
      <rect x="538" y="120" width="171" height="161" fill="url(#wood)"/>
    </svg>

    <h1 class="cover__title">
      <span>The</span>
      <span>Secure</span>
      <span>Leader</span>
    </h1>

    <p class="cover__subtitle">
      <span>Discover how your attachment style</span>
      <span>impact relationships with your team members</span>
      <span>and their wellbeing and performance</span>
    </p>

    <div class="publisher">
      <span class="publisher__name">finch learning</span>
    </div>

    <p class="cover__author">Tova Lund</p>
  </main>
</body>
</html>
```